Book Title: The Harvest Lantern. Author Name: Marisa Thornbury

We are needing a cover, spine and back cover design for a poetry book that we are publishing called The Harvest Lantern. We are looking for an elegant, and simplistic design with a very natural, dynamic and powerful impact.

Design Idea #1 - Shiva Conch Shell with a pink or black background. See Colin Vesey Image attached for design inspiration. Simple and dynamic .
Title and Author name created in same style as the attached Colin Vesey's Ledgers and Lanterns image.

Design Idea #2 - Image of cauldron on (see cauldrons attached for ideas) black background.
See Colin Vesey Image attached for design inspiration. Simple and dynamic Title and Author name created in same style as the attached Colin Vesey's Ledgers and Lanterns image

Design Idea #3 - Image of Tree of Life (see attached images for idea of what we are looking for) Would like to see on plain white, green, black and green background.

Target Market(s)

Spiritual Women, healers, visionaries,Goddess'

Requirements
Must have
• Please see project descriptions for specific design concepts we are looking for. Please include the authors name: Marisa Thornbury on front, spine and back cover of the book

```html
<!DOCTYPE html>
<html lang="en">
<head>
<meta charset="utf-8">
<title>The Harvest Lantern – Cover Spread</title>
<link href="https://fonts.googleapis.com/css2?family=Playfair+Display:wght@400;700&family=Montserrat:wght@500;600&display=swap" rel="stylesheet">
<style>
  :root {
    --bg: #d1d3d4;
    --leaf: #84c042;
    --leaf-shade: #6ea133;
    --paper: #ffffff;
    --ink: #111111;
    --tree-dark: #151515;
    --tree-mid: #3a3a3a;
  }
  * { margin: 0; padding: 0; box-sizing: border-box; }
  html, body {
    width: 1200px;
    height: 961px;
    overflow: hidden;
    background: var(--bg);
  }
  .spread {
    position: absolute;
    left: 121px;
    top: 124px;
    width: 958px;
    height: 713px;
    display: flex;
  }
  .back-cover {
    position: relative;
    width: 447px;
    height: 100%;
    background: var(--leaf);
  }
  .back-author {
    position: absolute;
    left: 0;
    bottom: 64px;
    width: 100%;
    text-align: center;
    font-family: "Montserrat", sans-serif;
    font-weight: 500;
    font-size: 13px;
    letter-spacing: 3px;
    color: var(--paper);
    text-transform: uppercase;
  }
  .spine {
    position: relative;
    width: 66px;
    height: 100%;
    background: linear-gradient(to right,
      var(--leaf) 0%,
      var(--leaf-shade) 10%,
      var(--leaf) 40%,
      var(--leaf) 100%);
  }
  .spine-title,
  .spine-author {
    position: absolute;
    left: 50%;
    writing-mode: vertical-rl;
    transform: translateX(-50%);
    white-space: nowrap;
  }
  .spine-title {
    top: 81px;
    font-family: "Playfair Display", serif;
    font-size: 25px;
    color: var(--paper);
    line-height: 1;
  }
  .spine-title .small { font-size: 15px; }
  .spine-author {
    top: 493px;
    font-family: "Montserrat", sans-serif;
    font-weight: 600;
    font-size: 12px;
    letter-spacing: 1px;
    color: var(--ink);
    line-height: 1;
  }
  .front-cover {
    position: relative;
    width: 445px;
    height: 100%;
    background: var(--paper);
  }
  .front-title {
    position: absolute;
    top: 102px;
    left: 0;
    width: 100%;
    text-align: center;
    font-family: "Playfair Display", serif;
    font-weight: 700;
    color: var(--ink);
    text-transform: uppercase;
  }
  .front-title .line-the {
    display: block;
    font-size: 31px;
    line-height: 36px;
    letter-spacing: 5px;
  }
  .front-title .line-main {
    display: block;
    font-size: 37px;
    line-height: 38px;
    letter-spacing: 6px;
  }
  .front-title .line-the + .line-main { margin-top: -3px; }
  .emblem {
    position: absolute;
    left: 0;
    top: 0;
    width: 445px;
    height: 713px;
  }
  .author-band {
    position: absolute;
    left: 0;
    top: 621px;
    width: 100%;
    height: 28px;
    background: var(--leaf);
    display: flex;
    align-items: center;
    justify-content: center;
    font-family: "Montserrat", sans-serif;
    font-weight: 500;
    font-size: 14px;
    letter-spacing: 3px;
    color: var(--paper);
    text-transform: uppercase;
  }
</style>
</head>
<body>
  <div class="spread">
    <section class="back-cover">
      <p class="back-author">Marisa Thornbury</p>
    </section>

    <section class="spine">
      <div class="spine-title"><span class="small">THE</span> HARVEST LANTERN</div>
      <div class="spine-author">MARISA THORNBURY</div>
    </section>

    <section class="front-cover">
      <h1 class="front-title">
        <span class="line-the">The</span>
        <span class="line-main">Harvest</span>
        <span class="line-main">Lantern</span>
      </h1>

      <svg class="emblem" viewBox="0 0 445 713" xmlns="http://www.w3.org/2000/svg">
        <defs>
          <radialGradient id="tree-tone" cx="50%" cy="50%" r="50%">
            <stop offset="0%" stop-color="var(--tree-mid)"/>
            <stop offset="100%" stop-color="var(--tree-dark)"/>
          </radialGradient>
        </defs>
        <path class="crescent" d="M91 354 Q221.5 148 352 354 Q221.5 186 91 354 Z" fill="var(--leaf)"/>
        <circle class="tree-of-life" cx="221" cy="424" r="133" fill="url(#tree-tone)"
                role="img" aria-label="Black Celtic tree of life with knotted roots and leafy branches inside a circle"/>
      </svg>

      <div class="author-band">Marisa Thornbury</div>
    </section>
  </div>
</body>
</html>
```